web page design with coding

We are a start up insurance agency who needs to design a full functional web page. we recently did a postcard design though brightloom I will upload the final project for you to see the color scheme/font we would like to continue to use. I also have a rough draft of verbage I would like our website to have. I will upload that as well.

Reason: I am sorry but the person who will make the final decision on the website is out of the country at the moment and will make the final decision when he returns.

Insurance

```html
<!DOCTYPE html>
<html lang="en">
<head>
<meta charset="utf-8">
<title>Veritas Cover Group</title>
<link href="https://fonts.googleapis.com/css2?family=Roboto:ital,wght@0,400;0,500;0,700;1,400&display=swap" rel="stylesheet">
<style>
:root{
  --navy:#1d2a4a;
  --nav-blue:#1c4b8c;
  --nav-blue-dark:#173e75;
  --green:#17962f;
  --green-dark:#0f7d25;
  --sky-blue:#2a8fd0;
  --header-grey:#e5e5e5;
  --section-grey:#f3f3f3;
  --text:#666;
  --heading:#1b1b1b;
  --footer-top:#3b78c6;
  --footer-bottom:#2b61ad;
}
*{margin:0;padding:0;box-sizing:border-box}
html,body{width:780px;height:1200px;overflow:hidden;background:#fff}
body{position:relative;font-family:'Roboto',sans-serif;color:var(--text)}
.abs{position:absolute}
.site-header{left:0;top:0;width:780px;height:90px;background:var(--header-grey)}
.brand{left:49px;top:30px;display:flex;align-items:center;gap:8px;font-size:20px;font-weight:500;color:var(--navy)}
.brand-dot{width:14px;height:14px;background:var(--navy);border-radius:50%}
.call{left:500px;top:16px;width:254px;text-align:center}
.call-lead{font-size:12.5px;color:#222}
.call-offer{font-size:15px;color:var(--sky-blue);margin-top:1px}
.call-phone{display:flex;align-items:center;justify-content:center;gap:8px;font-size:16px;font-weight:500;color:var(--navy);margin-top:3px}
.main-nav{left:0;top:90px;width:780px;height:35px;background:linear-gradient(var(--nav-blue),var(--nav-blue-dark))}
.main-nav a{position:absolute;top:0;height:35px;line-height:35px;font-size:8.4px;color:#fff;text-decoration:none;transform:translateX(-50%);white-space:nowrap}
.main-nav a.active{left:48px;width:66px;transform:none;text-align:center;background:var(--green)}
.hero{left:0;top:125px;width:780px;height:345px;background:linear-gradient(180deg,#dfe6ea 0%,#c9d3cf 30%,#a7a86c 55%,#caa45a 75%,#d9b776 100%)}
.hero-wave{left:0;top:340px}
.welcome-title{left:0;top:485px;width:780px;text-align:center;font-size:19px;font-weight:500;color:var(--heading)}
.title-rule{left:381px;top:510px;width:18px;height:2px;background:var(--green)}
.welcome-text{left:61px;top:525px;width:657px;text-align:center;font-size:8.8px;line-height:14.4px}
.service{top:589px;width:290px;text-align:center}
.service-photo{width:140px;height:140px;border-radius:50%;margin:0 auto;border:3px solid #e9ece9}
.service-photo.business{background:radial-gradient(circle at 45% 40%,#9ed14a,#3e8a1c 75%)}
.service-photo.personal{background:radial-gradient(circle at 50% 45%,#e6e2dc,#9da7b4 80%)}
.service h3{font-size:11px;font-weight:400;color:var(--heading);margin-top:17px}
.service p{font-size:8.6px;line-height:13px;margin-top:8px}
.btn{display:inline-block;width:85px;height:23px;line-height:23px;text-align:center;font-size:8px;color:#fff;background:linear-gradient(var(--green),var(--green-dark));border-radius:2px;text-decoration:none}
.service .btn{margin-top:14px}
.about-band{left:0;top:866px;width:780px;height:274px;background:var(--section-grey)}
.about{left:49px;top:901px;width:392px}
.about h2,.agent h2{font-size:19px;font-weight:400;color:var(--heading);letter-spacing:.3px}
.about p{font-size:8.5px;line-height:14.4px;margin-top:14px}
.about p:first-of-type{margin-top:15px}
.about .btn{margin-top:12px}
.agent{left:458px;top:905px;width:273px;height:199px;background:#fff}
.agent-info{position:absolute;left:16px;top:17px;width:160px}
.agent-name{font-size:14px;font-style:italic;color:var(--green);margin-top:11px}
.agent-bio{font-size:8px;line-height:14.4px;margin-top:3px}
.agent-bio b{font-weight:500;color:var(--navy);font-size:10px}
.agent .btn{margin-top:10px}
.agent-photo{position:absolute;left:170px;top:15px;width:100px;height:184px;background:linear-gradient(180deg,#e8d3b9,#b98a58 60%,#8a6440);border-radius:50px 50px 0 0}
.site-footer{left:0;top:1140px;width:780px;height:60px;background:linear-gradient(var(--footer-top),var(--footer-bottom));color:#fff}
.footer-links{position:absolute;left:49px;top:16px;font-size:8.6px}
.footer-links span{margin:0 6px}
.copyright{position:absolute;left:49px;top:31px;font-size:8.6px}
.social{position:absolute;left:610px;top:21px;display:flex;gap:6px}
.social i{width:19px;height:19px;border-radius:50%;background:#fff;display:block}
</style>
</head>
<body>
<header class="site-header abs">
  <div class="brand abs"><span class="brand-dot"></span>Veritas Cover Group</div>
  <div class="call abs">
    <div class="call-lead">Call today for your</div>
    <div class="call-offer">no obligation insurance analysis</div>
    <div class="call-phone">
      <svg width="19" height="19" viewBox="0 0 20 20" aria-hidden="true"><circle cx="10" cy="10" r="8.8" fill="none" stroke="#17962f" stroke-width="1.6"/><path d="M7 5.5c.6-.3 1 .1 1.3.7l.6 1.3c.2.5 0 .9-.4 1.2l-.4.3c.5 1.2 1.4 2.1 2.6 2.7l.3-.4c.3-.4.7-.6 1.2-.4l1.3.6c.6.3 1 .7.7 1.3-.5 1-1.4 1.6-2.5 1.2C9.3 13.3 6.7 10.7 6 8c-.3-1.1.1-2 1-2.5z" fill="#17962f"/></svg>
      (555) 014-2276
    </div>
  </div>
</header>

<nav class="main-nav abs">
  <a class="active">HOME</a>
  <a style="left:153px">ABOUT US</a>
  <a style="left:226px">SERVICES</a>
  <a style="left:291px">BLOG</a>
  <a style="left:363px">LATEST NEWS</a>
  <a style="left:457px">OUR CLIENTS</a>
  <a style="left:540px">GALERY</a>
  <a style="left:614px">CONTACT US</a>
</nav>

<div class="hero abs" role="img" aria-label="Hand holding a small model house with an orange roof in front of a blurred field"></div>
<svg class="hero-wave abs" width="780" height="130" viewBox="0 0 780 130" aria-hidden="true">
  <path d="M0,116 C100,60 260,60 456,122 C560,130 680,120 780,96 L780,130 L0,130Z" fill="#fff"/>
  <path d="M0,84 C90,30 220,20 340,60 C420,85 500,80 620,60 C700,45 750,25 780,12 L780,96 C680,120 560,130 456,122 C260,60 100,60 0,116Z" fill="#17962f"/>
  <path d="M0,100 C110,50 260,50 456,122" fill="none" stroke="#fff" stroke-width="1.5"/>
</svg>

<h1 class="welcome-title abs">WELCOME TO VCG</h1>
<div class="title-rule abs"></div>
<p class="welcome-text abs">Veritas Cover Group has joined with regional &amp; national insurance companies to provide quality products and superior service. We take the time to discuss options and coverages, not to just sell insurance products. We strive to educate you in the decision making process to become an informed consumer. We specialize in commercial business &amp; personal insurance. We are committed to providing personal attention to all your insurance needs.</p>

<section class="service abs" style="left:77px">
  <div class="service-photo business" role="img" aria-label="Hands exchanging an umbrella and briefcase symbol over a green background"></div>
  <h3>BUSINESS INSURANCE</h3>
  <p>Veritas Cover Group is a one stop shop for all of your personal<br>and business insurance needs. With our established relationships and<br>market knowledge, we will tailor an insurance.</p>
  <a class="btn">LEARN MORE</a>
</section>
<section class="service abs" style="left:413px">
  <div class="service-photo personal" role="img" aria-label="Couple reviewing insurance paperwork at a table"></div>
  <h3>PERSONAL INSURANCE</h3>
  <p>Veritas Cover Group is a one stop shop for all of your personal<br>and business insurance needs. With our established relationships and<br>market knowledge, we will tailor an insurance.</p>
  <a class="btn">LEARN MORE</a>
</section>

<div class="about-band abs"></div>
<section class="about abs">
  <h2>ABOUT US</h2>
  <p>Established in 2015, Veritas Cover Group is a full service independent insurance agency. Our licensed agents have the experience to custom tailor a program to meet your specific needs &amp; our professional support staff will provide you with top notch customer service to help ease the burden of managing your insurance program.</p>
  <p>We have established relationships with carriers in order to offer you the most competitive products and services available in the marketplace today.</p>
  <p>We look forward to working with you!</p>
  <a class="btn">LEARN MORE</a>
</section>

<section class="agent abs">
  <div class="agent-info">
    <h2>OUR AGENT</h2>
    <div class="agent-name">“Marla”</div>
    <p class="agent-bio"><b>Bio’s:</b> Sed ut perspiciatis unde omnis iste natus error sit voluptatem accus antium doloremque laudantium, totam rem aperiam, eaque ipsa quae ab illo inventore veritatis et quasi architecto.</p>
    <a class="btn">KNOW MORE</a>
  </div>
  <div class="agent-photo" role="img" aria-label="Portrait of the agent in a brown jacket with arms crossed"></div>
</section>

<footer class="site-footer abs">
  <div class="footer-links">Home<span>|</span>About Us<span>|</span>Services<span>|</span>Clients<span>|</span>Contact</div>
  <div class="copyright">Copyright © 2016. All right reserved</div>
  <div class="social" aria-label="Social links"><i></i><i></i><i></i><i></i><i></i></div>
</footer>
</body>
</html>
```